Travel Activities - Tours, sightseeing tours, activities & things to do website design

We need a web design that covers Tours, sightseeing tours, activities and things to do in the travel industry. Need to be a simple design with good SEO technical structure and conversion optimised design.
Inspirations
Similar site - https://www.wandoro.com/London/d512-ttd?pub=KRT8VX_4_7
Design and layout - https://www.stayplumo.com.au/europe-294/hotel
Colours - please suggest ( prefer happy energetic colours )
Pages
1. Home page design
2. Individual tour or activity page design
Target Market(s)
Independent travellers who want to plan the holiday by themselfs.
Industry/Entity Type
Travel Industry
Number of Pages Required
2 page
Colors
Designer to choose colors to be used in the design.
Requirements
Must have
- Pages
- 1. Home page design
- 2. Individual tour or activity page design
- SEO
- H1 tags
- Text Descriptions
- Internal linking to other tours activities

```html
<!DOCTYPE html>
<html lang="en">
<head>
<meta charset="utf-8">
<title>Roamwell – Tours, Sightseeing &amp; Things to Do</title>
<link rel="stylesheet" href="https://fonts.googleapis.com/css2?family=Mulish:wght@400;600;700&family=Zilla+Slab:wght@600&display=swap">
<style>
:root{
  --navy-dark:#0a2a6b;
  --navy:#0f3c91;
  --blue:#1668c8;
  --blue-btn:#1a6dd0;
  --footer:#1a6cc9;
  --footer-base:#155fb8;
  --orange:#f5a300;
  --orange-btn:#ff9800;
  --page:#ebebeb;
  --white:#fff;
  --ink:#222;
  --muted:#8c8c8c;
  --line:#d6d6d6;
  --soft:#f3f3f3;
}
*{margin:0;padding:0;box-sizing:border-box}
html,body{width:678px;height:1200px;overflow:hidden;background:var(--page)}
body{font-family:"Mulish",Arial,sans-serif;color:var(--ink)}
.page{position:relative;width:678px;height:1200px;overflow:hidden;background:var(--page)}
a{color:inherit;text-decoration:none}
.abs{position:absolute}

/* header */
.utility-bar{left:0;top:0;width:678px;height:22px;background:var(--navy-dark)}
.utility-links{right:66px;top:5px;font-size:7.5px;color:#dfe8ff;display:flex;gap:5px;align-items:center}
.cart{display:flex;align-items:center;gap:2px;font-weight:700;margin-left:8px;color:#fff}
.main-nav{left:0;top:22px;width:678px;height:46px;background:var(--navy)}
.brand{left:70px;top:8px;font-family:"Zilla Slab",Georgia,serif;font-weight:600;font-size:21px;color:#fff;letter-spacing:.3px}
.nav-links{top:15px;left:288px;font-size:9.5px;color:#cfdcff;display:flex;gap:0}
.nav-links a{position:absolute;white-space:nowrap}
.nav-links .active{color:#fff;font-weight:700}
.nav-search{left:591px;top:11px;width:21px;height:21px;border-radius:50%;background:var(--orange);display:flex;align-items:center;justify-content:center}

/* hero */
.hero{left:0;top:68px;width:678px;height:225px;overflow:hidden}
.hero-photo{position:absolute;inset:0;background:linear-gradient(180deg,#0a1e55 0%,#1b2f6a 35%,#6b4a2a 65%,#b87a22 85%,#5a3a18 100%)}
.hero h1{position:absolute;top:54px;width:100%;text-align:center;font-size:20.5px;font-weight:600;color:#fff}
.hero .tagline{position:absolute;top:82px;width:100%;text-align:center;font-size:13.5px;font-weight:600;color:#fff}
.search-form{position:absolute;left:123px;top:105px;width:432px;height:28px;display:flex}
.search-keyword{width:241px;background:#fff;display:flex;align-items:center;padding-left:8px;gap:5px;font-size:9.5px;color:#666}
.search-location{width:120px;background:#ececec;display:flex;align-items:center;justify-content:space-between;padding:0 10px;font-size:9.5px;color:#777}
.search-btn{width:71px;background:var(--orange);color:#fff;font-size:11.5px;font-weight:600;display:flex;align-items:center;justify-content:center}
.slider-dots{position:absolute;top:201px;left:313px;display:flex;gap:5px}
.slider-dots span{width:9px;height:9px;border-radius:50%;background:#fff;border:1.5px solid #fff}
.slider-dots span:first-child{background:transparent}

/* sidebar */
.panel{background:#fff;border:1px solid #dcdcdc;box-shadow:0 0 3px rgba(0,0,0,.08)}
.find-tour{left:66px;top:314px;width:144px;height:168px}
.find-tour h2{position:absolute;left:13px;top:15px;font-size:12.5px;font-weight:600;color:var(--orange)}
.field{position:absolute;height:18px;border:1px solid var(--line);font-size:6px;color:#888;padding:5px 0 0 7px}
.find-btn{position:absolute;left:12px;top:131px;width:121px;height:18px;background:var(--blue-btn);color:#fff;font-size:7.5px;display:flex;align-items:center;justify-content:center}
.categories{left:66px;top:498px;width:144px;height:292px}
.categories h2{position:absolute;left:17px;top:12px;font-size:12.5px;font-weight:600;color:#222}
.categories ul{position:absolute;left:20px;top:40px;list-style:none}
.categories li{height:18.6px;font-size:7.2px;color:#666;display:flex;align-items:center;gap:6px}
.categories li::before{content:"";border-left:3px solid #aaa;border-top:3px solid transparent;border-bottom:3px solid transparent}

/* featured */
.section-title{left:225px;top:320px;font-size:15px;font-weight:400;color:#333}
.card{position:absolute;width:122px;height:186px;background:#fff}
.card .photo{position:absolute;left:0;top:0;width:122px;height:86px}
.card h3{position:absolute;left:12px;top:91px;font-size:10px;font-weight:600;color:var(--blue)}
.card .desc{position:absolute;left:13px;top:105px;width:106px;font-size:5.4px;line-height:10px;color:#999}
.card .stars{position:absolute;left:12px;top:141px;font-size:9px;color:var(--orange);letter-spacing:-.5px}
.card .loc{position:absolute;left:68px;top:144px;font-size:6.4px;color:#888}
.card .price-row{position:absolute;left:0;top:164px;width:122px;height:22px;background:var(--soft)}
.card .price{position:absolute;left:14px;top:5px;font-size:9.5px;font-weight:600;color:#222}
.card .book{position:absolute;left:62px;top:0;width:60px;height:21px;background:var(--orange-btn);color:#fff;font-size:7.4px;display:flex;align-items:center;justify-content:center}

/* footer */
.site-footer{left:0;top:977px;width:678px;height:183px;background:var(--footer);color:#fff}
.foot-col{position:absolute;top:35px}
.foot-col h4{font-size:11.5px;font-weight:600;margin-bottom:9px}
.foot-col a{display:block;font-size:7.8px;color:#e3eeff;height:17.6px}
.contact-line{display:flex;align-items:flex-start;gap:8px;font-size:7.8px;color:#e3eeff;height:17.6px}
.contact-line .ico{width:13px;display:flex;justify-content:center}
.social{display:flex;gap:3px;margin-top:1px}
.social span{width:18px;height:18px;border-radius:50%;border:1.2px solid #fff}
.footer-base{left:0;top:1160px;width:678px;height:40px;background:var(--footer-base);color:#e3eeff;font-size:6.8px;text-align:center;padding-top:14px}
</style>
</head>
<body>
<div class="page">

  <header>
    <div class="utility-bar abs">
      <nav class="utility-links abs">
        <a href="#">Login</a><span>|</span><a href="#">Register</a><span>|</span><a href="#">Help</a>
        <a class="cart" href="#">
          <svg width="13" height="10" viewBox="0 0 13 10" fill="none" stroke="#fff" stroke-width="1.1"><path d="M0.5 1h2l1.6 6h6.4l1.5-4.5H3.3"/><circle cx="5" cy="8.8" r=".9" fill="#fff"/><circle cx="9.6" cy="8.8" r=".9" fill="#fff"/></svg>
          My Cart
        </a>
      </nav>
    </div>
    <div class="main-nav abs">
      <a class="brand abs" href="#">Roamwell</a>
      <nav class="nav-links abs">
        <a class="active" href="#" style="left:0">Home</a>
        <a href="#" style="left:46px">About Us</a>
        <a href="#" style="left:106px">Search Now</a>
        <a href="#" style="left:180px">Support</a>
        <a href="#" style="left:235px">Resources</a>
      </nav>
      <a class="nav-search abs" href="#" aria-label="Search">
        <svg width="10" height="10" viewBox="0 0 10 10" fill="none" stroke="#fff" stroke-width="1.6"><circle cx="4.2" cy="4.2" r="3"/><path d="M6.4 6.4L9 9"/></svg>
      </a>
    </div>
  </header>

  <section class="hero abs">
    <div class="hero-photo" role="img" aria-label="Ornate honeycomb palace facade lit golden against a deep blue evening sky"></div>
    <h1>Aonubia nostra inceptos hymenaeos</h1>
    <p class="tagline">Proin nulla arcu nonummy luctus dictum</p>
    <form class="search-form">
      <div class="search-keyword">
        <svg width="10" height="10" viewBox="0 0 10 10" fill="none" stroke="#999" stroke-width="1.3"><circle cx="4.2" cy="4.2" r="3"/><path d="M6.4 6.4L9 9"/></svg>
        Enter Keyword
      </div>
      <div class="search-location">Location
        <svg width="10" height="6" viewBox="0 0 10 6" fill="none" stroke="#999" stroke-width="1"><path d="M1 1l4 4 4-4"/></svg>
      </div>
      <div class="search-btn">Search</div>
    </form>
    <div class="slider-dots"><span></span><span></span><span></span><span></span></div>
  </section>

  <aside>
    <div class="find-tour panel abs">
      <h2>Find a Tour</h2>
      <div class="field" style="left:12px;top:37px;width:121px">Tour Tittle</div>
      <div class="field" style="left:12px;top:61px;width:121px">Location</div>
      <div class="field" style="left:12px;top:84px;width:60px">From</div>
      <div class="field" style="left:74px;top:84px;width:59px">To</div>
      <div class="field" style="left:12px;top:108px;width:121px">Select Price</div>
      <div class="find-btn">SEARCH</div>
    </div>
    <div class="categories panel abs">
      <h2>Our Categories</h2>
      <ul>
        <li>Praesent elementum</li>
        <li>Elit at tellus nec ultricies</li>
        <li>Sit amet porttitor</li>
        <li>Aattis enim In</li>
        <li>Passa libero interdum</li>
        <li>Nec interdum vel</li>
        <li>Blandit sed nulla</li>
        <li>In ullamcorper est</li>
        <li>Aget tempor cursus</li>
        <li>Neque mi consectetuer</li>
        <li>Ai a ultricies massa</li>
        <li>Est sed nisl Class</li>
        <li>Aptent taciti sociosqu</li>
      </ul>
    </div>
  </aside>

  <main>
    <h2 class="section-title abs">Featured Tours</h2>

    <article class="card" style="left:226px;top:350px">
      <div class="photo" role="img" aria-label="White villa with a blue pool at sunset" style="background:linear-gradient(180deg,#6fa2d8,#e2d6c2 55%,#3a6aa8)"></div>
      <h3>Tour Tittle here</h3>
      <p class="desc">ullamcorper est eget tempor cursus neque mi consectetuer mi a ultricies massa est sed nisl Class</p>
      <div class="stars">★★★★</div><div class="loc">Location City</div>
      <div class="price-row"><span class="price">$125.99</span><a class="book" href="#">Book Now</a></div>
    </article>
    <article class="card" style="left:358px;top:350px">
      <div class="photo" role="img" aria-label="Infinity pool overlooking a blue sea and islands" style="background:linear-gradient(180deg,#4a9be0,#8fcdf0 50%,#2a8fc8)"></div>
      <h3>Tour Tittle here</h3>
      <p class="desc">ullamcorper est eget tempor cursus neque mi consectetuer mi a ultricies massa est sed nisl Class</p>
      <div class="stars">★★★★</div><div class="loc">Location City</div>
      <div class="price-row"><span class="price">$125.99</span><a class="book" href="#">Book Now</a></div>
    </article>
    <article class="card" style="left:490px;top:350px">
      <div class="photo" role="img" aria-label="Resort pool with umbrellas at dusk" style="background:linear-gradient(180deg,#e8a070,#8a6a6a 45%,#2f6e8e)"></div>
      <h3>Tour Tittle here</h3>
      <p class="desc">ullamcorper est eget tempor cursus neque mi consectetuer mi a ultricies massa est sed nisl Class</p>
      <div class="stars">★★★★</div><div class="loc">Location City</div>
      <div class="price-row"><span class="price">$125.99</span><a class="book" href="#">Book Now</a></div>
    </article>

    <article class="card" style="left:226px;top:550px">
      <div class="photo" role="img" aria-label="Seaside terrace with lounge chairs" style="background:linear-gradient(180deg,#5fb3dc,#9fd3e8 50%,#d8d2c6)"></div>
      <h3>Tour Tittle here</h3>
      <p class="desc">ullamcorper est eget tempor cursus neque mi consectetuer mi a ultricies massa est sed nisl Class</p>
      <div class="stars">★★★★</div><div class="loc">Location City</div>
      <div class="price-row"><span class="price">$125.99</span><a class="book" href="#">Book Now</a></div>
    </article>
    <article class="card" style="left:358px;top:550px">
      <div class="photo" role="img" aria-label="Hotel bedroom with a dark headboard and white bed" style="background:linear-gradient(180deg,#5a3426,#8a5a3e 50%,#e6ddd2)"></div>
      <h3>Tour Tittle here</h3>
      <p class="desc">ullamcorper est eget tempor cursus neque mi consectetuer mi a ultricies massa est sed nisl Class</p>
      <div class="stars">★★★★</div><div class="loc">Location City</div>
      <div class="price-row"><span class="price">$125.99</span><a class="book" href="#">Book Now</a></div>
    </article>
    <article class="card" style="left:490px;top:550px">
      <div class="photo" role="img" aria-label="Sail-shaped tower hotel by the sea at twilight" style="background:linear-gradient(180deg,#5f7fb8,#9ab0d6 55%,#3a5a8c)"></div>
      <h3>Tour Tittle here</h3>
      <p class="desc">ullamcorper est eget tempor cursus neque mi consectetuer mi a ultricies massa est sed nisl Class</p>
      <div class="stars">★★★★</div><div class="loc">Location City</div>
      <div class="price-row"><span class="price">$125.99</span><a class="book" href="#">Book Now</a></div>
    </article>

    <article class="card" style="left:226px;top:753px">
      <div class="photo" role="img" aria-label="Ancient columned temple ruins under a cloudy sky" style="background:linear-gradient(180deg,#7d8fb8,#c9a57a 55%,#8a6a42)"></div>
      <h3>Tour Tittle here</h3>
      <p class="desc">ullamcorper est eget tempor cursus neque mi consectetuer mi a ultricies massa est sed nisl Class</p>
      <div class="stars">★★★★</div><div class="loc">Location City</div>
      <div class="price-row"><span class="price">$125.99</span><a class="book" href="#">Book Now</a></div>
    </article>
    <article class="card" style="left:358px;top:753px">
      <div class="photo" role="img" aria-label="Colourful street market with a large festive statue" style="background:linear-gradient(180deg,#5a90c8,#c46a3a 55%,#6a4a3a)"></div>
      <h3>Tour Tittle here</h3>
      <p class="desc">ullamcorper est eget tempor cursus neque mi consectetuer mi a ultricies massa est sed nisl Class</p>
      <div class="stars">★★★★</div><div class="loc">Location City</div>
      <div class="price-row"><span class="price">$125.99</span><a class="book" href="#">Book Now</a></div>
    </article>
    <article class="card" style="left:490px;top:753px">
      <div class="photo" role="img" aria-label="Tall waterfall over green cliffs" style="background:linear-gradient(90deg,#3a5a3a,#a8c8d8 55%,#4a7a4a)"></div>
      <h3>Tour Tittle here</h3>
      <p class="desc">ullamcorper est eget tempor cursus neque mi consectetuer mi a ultricies massa est sed nisl Class</p>
      <div class="stars">★★★★</div><div class="loc">Location City</div>
      <div class="price-row"><span class="price">$125.99</span><a class="book" href="#">Book Now</a></div>
    </article>
  </main>

  <footer class="site-footer abs">
    <div class="foot-col" style="left:68px">
      <h4>Quick Links</h4>
      <a href="#">Home</a><a href="#">About Us</a><a href="#">Our Tours</a><a href="#">Book Now</a>
    </div>
    <div class="foot-col" style="left:177px">
      <h4>Resources</h4>
      <a href="#">Donec dictum</a><a href="#">Rectus non</a><a href="#">Ddio Cras a</a><a href="#">Pnte vitae</a>
    </div>
    <div class="foot-col" style="left:286px">
      <h4>Sublinks</h4>
      <a href="#">Allamcorper est</a><a href="#">Eget tempor</a><a href="#">Cursus neque</a><a href="#">Aonsectetuer mi</a><a href="#">Lltricies massa</a>
    </div>
    <div class="foot-col" style="left:401px">
      <h4>Support</h4>
      <a href="#">Support</a><a href="#">FAQ</a><a href="#">Blogs</a><a href="#">Contact</a>
    </div>
    <div class="foot-col" style="left:491px">
      <h4>Contact Us</h4>
      <div class="contact-line"><span class="ico"><svg width="8" height="11" viewBox="0 0 8 11" fill="none" stroke="#fff" stroke-width="1.1"><path d="M4 10.3C1.8 7.4.6 5.6.6 4A3.4 3.4 0 0 1 7.4 4c0 1.6-1.2 3.4-3.4 6.3z"/><circle cx="4" cy="4" r="1.2"/></svg></span>48 Harbor Lane #4B</div>
      <div class="contact-line"><span class="ico"></span>Texas 75001 TX</div>
      <div class="contact-line"><span class="ico"><svg width="11" height="11" viewBox="0 0 11 11" fill="none" stroke="#fff" stroke-width="1"><path d="M2.3.8l1.8 2.2-1 1.3a6.5 6.5 0 0 0 3.6 3.6l1.3-1 2.2 1.8-1 1.6C5.3 10.1.9 5.7.7 1.8z"/></svg></span>555.014.2290</div>
      <div class="contact-line"><span class="ico"><svg width="11" height="8" viewBox="0 0 11 8" fill="none" stroke="#fff" stroke-width="1"><rect x=".5" y=".5" width="10" height="7"/><path d="M.5.5l5 4 5-4"/></svg></span>info@roamwell.com</div>
      <div class="social" style="margin-left:11px"><span></span><span></span><span></span><span></span></div>
    </div>
  </footer>
  <div class="footer-base abs">© 2017 Roamwell  All right reserved  Term of Use</div>

</div>
</body>
</html>
```